Modern corporate energy/fuel business need business card design

Business card required for company founder. Korvan Fuel Partners is a Australian based modern energy/fuel provider. We offer specialised solutions to businesses using fossil fuels through renewable energy solutions.

I would like one side with specific information (name, address etc)

The other side to be bold, professional company name & logo. Striking.

Target Market(s)

B2B. Transport, mining, councils, environmentalist,

Industry/Entity Type

Petroleum

Contact Information for Business Card

Name; Peter Morrow
Position; Director
Email; pmorrow@korvanse.com.au
Address; PO Box 347, Tallowmere, QLD, 4890
Website; www.korvanse.com.au

Colors

Designer to choose colors to be used in the design.

Requirements
Must have
• Clean, easy to read, professional & strong theme
Should not have
• too many colours, busy layout,

```html
<!DOCTYPE html>
<html lang="en">
<head>
<meta charset="utf-8">
<title>Korvan Fuel Partners – Business Card</title>
<link href="https://fonts.googleapis.com/css2?family=Montserrat:wght@600;800&family=Roboto:wght@400&display=swap" rel="stylesheet">
<style>
  :root {
    --navy: #1d4e75;
    --orange: #f26f22;
    --orange-light: #f7953f;
    --paper: #ffffff;
    --backdrop: #1f1f1f;
  }
  * { margin: 0; padding: 0; box-sizing: border-box; }
  html, body {
    width: 1200px; height: 1200px; overflow: hidden;
    background: var(--backdrop);
  }
  .stage { position: relative; width: 1200px; height: 1200px; }
  .card {
    position: absolute; left: 150px; width: 900px; height: 514px;
    background: var(--paper); border-radius: 28px; overflow: hidden;
  }
  .card--front { top: 50px; }
  .card--back { top: 630px; }

  .brand-name {
    font-family: "Montserrat", sans-serif; font-weight: 800;
    color: var(--navy); text-transform: uppercase; letter-spacing: 3px;
    display: flex; align-items: center; gap: 20px; white-space: nowrap;
  }
  .brand-dot {
    display: inline-block; border-radius: 50%; background: var(--orange); flex: none;
  }
  .card--front .brand-name {
    position: absolute; top: 196px; left: 0; right: 0;
    justify-content: center; font-size: 42px;
  }
  .card--front .brand-dot { width: 84px; height: 84px; }
  .front-url {
    position: absolute; bottom: 58px; left: 0; right: 0; text-align: center;
    font-family: "Montserrat", sans-serif; font-weight: 600; font-size: 19px;
    color: var(--navy); letter-spacing: 1px; text-transform: uppercase;
  }

  .card--back .brand-name {
    position: absolute; top: 68px; left: 48px; font-size: 34px;
  }
  .card--back .brand-dot { width: 70px; height: 70px; }

  .back-shapes { position: absolute; inset: 0; }

  .person { position: absolute; left: 70px; top: 356px; }
  .person-name {
    font-family: "Montserrat", sans-serif; font-weight: 800; font-size: 30px;
    color: var(--navy); text-transform: uppercase; line-height: 1;
  }
  .person-role {
    font-family: "Montserrat", sans-serif; font-weight: 800; font-size: 22px;
    color: var(--orange); text-transform: uppercase; margin-top: 6px;
  }

  .contact-list {
    position: absolute; right: 70px; top: 318px; list-style: none;
    font-family: "Roboto", sans-serif; font-size: 24px; color: var(--paper);
  }
  .contact-item {
    display: flex; align-items: center; justify-content: flex-end;
    gap: 14px; height: 38px; white-space: nowrap;
  }
  .contact-icon {
    width: 30px; height: 30px; border-radius: 50%; background: var(--paper);
    display: flex; align-items: center; justify-content: center; flex: none;
  }
  .contact-icon svg { width: 18px; height: 18px; }
</style>
</head>
<body>
<main class="stage">

  <section class="card card--front" aria-label="Card front">
    <div class="brand-name"><span class="brand-dot"></span>Korvan Fuel Partners</div>
    <p class="front-url">www.korvanse.com.au</p>
  </section>

  <section class="card card--back" aria-label="Card back">
    <svg class="back-shapes" width="900" height="514" viewBox="0 0 900 514" aria-hidden="true">
      <circle cx="880" cy="760" r="560" fill="var(--orange)"/>
    </svg>

    <div class="brand-name"><span class="brand-dot"></span>Korvan Fuel Partners</div>

    <div class="person">
      <p class="person-name">Peter Morrow</p>
      <p class="person-role">Director</p>
    </div>

    <ul class="contact-list">
      <li class="contact-item">0700 555 0142
        <span class="contact-icon"><svg viewBox="0 0 24 24"><path fill="var(--orange)" d="M6.6 10.8a15.1 15.1 0 0 0 6.6 6.6l2.2-2.2c.3-.3.7-.4 1-.2 1.1.4 2.3.6 3.6.6.6 0 1 .4 1 1V20c0 .6-.4 1-1 1A17 17 0 0 1 3 4c0-.6.4-1 1-1h3.5c.6 0 1 .4 1 1 0 1.3.2 2.5.6 3.6.1.3 0 .7-.2 1z"/></svg></span>
      </li>
      <li class="contact-item">pmorrow@korvanse.com.au
        <span class="contact-icon"><svg viewBox="0 0 24 24"><rect x="3" y="6" width="18" height="12" rx="1.5" fill="none" stroke="var(--orange)" stroke-width="2"/><path d="M3.5 7l8.5 6 8.5-6" fill="none" stroke="var(--orange)" stroke-width="2"/></svg></span>
      </li>
      <li class="contact-item">www.korvanse.com.au
        <span class="contact-icon"><svg viewBox="0 0 24 24"><g fill="none" stroke="var(--orange)" stroke-width="1.8"><circle cx="12" cy="12" r="9"/><ellipse cx="12" cy="12" rx="4" ry="9"/><path d="M3 12h18M5 7h14M5 17h14"/></g></svg></span>
      </li>
      <li class="contact-item">PO Box 347, Tallowmere, QLD, 4890
        <span class="contact-icon"><svg viewBox="0 0 24 24"><path fill="var(--orange)" d="M12 2a7 7 0 0 0-7 7c0 5.2 7 13 7 13s7-7.8 7-13a7 7 0 0 0-7-7zm0 9.5A2.5 2.5 0 1 1 12 6.5a2.5 2.5 0 0 1 0 5z"/></svg></span>
      </li>
    </ul>
  </section>

</main>
</body>
</html>
```